MBA Banner Online Ad

I represent the MBA program department of China's #1 global business school, TOVRA. www.tovra.edu. We are looking for a designer to offer something unique, out of the box, yet maintaining the branding and reputation of our school. Our goal is to build a long-term relationship with our chosen designer for all the our department's design needs. The designer should provide amazing creativity, professionalism, and competitive pricing.

We are currently looking to design a flas banner add for MBA websites around the world with the following message. Add size is 300x350 pixels:

"In 1275 Edmund Varr set out to travel the world to discover China" Banner 1st Page

"Now is your chance to live and learn in China in order to discover the world" Banner 2nd Page

"TOVRA MBA - experience an elite business school with a new perspective" Banner 3rd Page

Our Logo and motto: "Rooted Minds, Open Horizons"

We need an add reflecting Edmund Varrs travels or Edmund Varr himself along with modern photos of Shanghai or our university, or whatever you suggest to reflect the message of modernity, elite organization, etc.

Please go according to our guidlines in the provided attachments.

Looking forward to your offers!
Updates

Current ad featured on :   http://lanternandledger.com/category/mba-rankings/

Want it replaced by a more creative and bold banner.

Project Deadline Extended
Reason: Awaiting a few more replies. Thanks

Target Market(s)

Prospective MBA Students

Industry/Entity Type

Travel

Requirements
Must have
• Color, fonts, etc, should go according to attached guidelines in the attachments provided. Please contact me directly should you have any questions or need any clarifications.

Ned

```html
<!DOCTYPE html>
<html lang="en">
<head>
<meta charset="utf-8">
<title>TOVRA MBA Banner</title>
<link rel="stylesheet" href="https://fonts.googleapis.com/css2?family=PT+Sans:wght@700&display=swap">
<style>
  :root {
    --backdrop: #000000;
    --frame: #f4f4f4;
    --red-top: #ec3a5c;
    --red-deep: #9a1320;
    --yellow: #e7d715;
    --yellow-light: #efe46a;
    --headline: #fff200;
    --text-light: #ffffff;
    --box-fill: rgba(225, 170, 20, 0.55);
  }
  * { margin: 0; padding: 0; box-sizing: border-box; }
  html, body {
    width: 1103px;
    height: 1200px;
    overflow: hidden;
    background: var(--backdrop);
  }
  .banner {
    position: relative;
    width: 1103px;
    height: 1200px;
    font-family: "PT Sans", "Myriad Pro", Arial, sans-serif;
    font-weight: 700;
  }
  .banner-art {
    position: absolute;
    inset: 0;
  }
  .headline {
    position: absolute;
    left: 163px;
    width: 792px;
    top: 150px;
    text-align: center;
    color: var(--headline);
    font-size: 72px;
    line-height: 110px;
    letter-spacing: 0.5px;
  }
  .message {
    position: absolute;
    display: flex;
    align-items: center;
    justify-content: center;
    text-align: center;
    color: var(--text-light);
    background: var(--box-fill);
    border-radius: 18px;
  }
  .message--story {
    left: 172px; top: 425px; width: 771px; height: 113px;
    font-size: 39px; line-height: 48px;
    background: rgba(205, 60, 40, 0.35);
  }
  .message--invite {
    left: 172px; top: 701px; width: 774px; height: 121px;
    font-size: 39px; line-height: 50px;
  }
  .message--signoff {
    left: 189px; top: 963px; width: 722px; height: 111px;
    font-size: 27px; line-height: 37px;
  }
</style>
</head>
<body>
<main class="banner">
  <svg class="banner-art" width="1103" height="1200" viewBox="0 0 1103 1200" aria-hidden="true">
    <defs>
      <linearGradient id="redFill" x1="0" y1="0" x2="0" y2="1">
        <stop offset="0" stop-color="var(--red-top)"/>
        <stop offset="1" stop-color="var(--red-deep)"/>
      </linearGradient>
      <linearGradient id="yellowFill" x1="0" y1="0" x2="0" y2="1">
        <stop offset="0" stop-color="#e4d20f"/>
        <stop offset="1" stop-color="var(--yellow)"/>
      </linearGradient>
      <linearGradient id="gloss" x1="0" y1="0" x2="0" y2="1">
        <stop offset="0" stop-color="#ffffff" stop-opacity="0.35"/>
        <stop offset="1" stop-color="#ffffff" stop-opacity="0.05"/>
      </linearGradient>
      <clipPath id="panelClip">
        <rect x="163" y="87" width="792" height="1013" rx="58"/>
      </clipPath>
    </defs>
    <rect class="frame" x="145" y="70" width="827" height="1047" rx="75" fill="var(--frame)"/>
    <g clip-path="url(#panelClip)">
      <rect x="163" y="87" width="792" height="1013" fill="url(#yellowFill)"/>
      <path d="M955 930 C 800 1010 600 1060 163 1100 L955 1100 Z" fill="var(--yellow-light)" opacity="0.6"/>
      <path d="M163 87 L955 87 L955 393 C 800 520 450 620 163 640 Z" fill="url(#redFill)"/>
      <path d="M163 87 L955 87 L955 140 C 780 150 600 260 163 300 Z" fill="url(#gloss)"/>
    </g>
  </svg>

  <h1 class="headline">ROOTED MINDS<br>OPEN HORIZONS</h1>
  <p class="message message--story">In 1275 Edmund Varr set out to travel<br>the world to discover China</p>
  <p class="message message--invite">Now is your chance to live and learn<br>in China in order to discover the world</p>
  <p class="message message--signoff">TOVRA MBA - experience an elite business school<br>with a new perspective</p>
</main>
</body>
</html>
```